Upscale business cards needed for family office

We would like professional business cards created for employees of our family office. Relatively simple and straightforward, but also with a unique element to set them apart. Probably stick with neutral and simple colors that mesh well with the colors in the logo. We need space for the traditional elements, including name, title, address, email/phone number.

Industry/Entity Type

Business

Contact Information for Business Card

Space for name, title, phone number, email, address

```html
<!DOCTYPE html>
<html lang="en">
<head>
<meta charset="utf-8">
<title>Ashby &amp; Lane — Business Cards</title>
<link rel="stylesheet" href="https://fonts.googleapis.com/css2?family=Quicksand:wght@500;600&display=swap">
<style>
  :root {
    --page: #ecebe8;
    --card-light: #ffffff;
    --card-dark: #141414;
    --ink: #1f1f1f;
    --accent: #1b8fc2;
    --mark-grey: #6b6e72;
    --mark-silver: #b9bcc0;
  }
  html, body {
    margin: 0;
    padding: 0;
    width: 1200px;
    height: 1200px;
    overflow: hidden;
    background: var(--page);
    font-family: "Quicksand", sans-serif;
  }
  .canvas {
    position: relative;
    width: 1200px;
    height: 1200px;
  }
  .card {
    position: absolute;
    left: 286px;
    width: 627px;
    height: 390px;
    box-shadow: 0 6px 18px rgba(0,0,0,0.12);
  }
  .card--front { top: 150px; background: var(--card-light); color: var(--ink); }
  .card--back  { top: 680px; background: var(--card-dark); }

  .brand {
    position: absolute;
    display: flex;
    align-items: center;
    gap: 10px;
    font-weight: 600;
    white-space: nowrap;
  }
  .brand__square {
    display: inline-block;
    border: 2px solid currentColor;
  }
  .card--front .brand {
    top: 40px;
    right: 30px;
    font-size: 24px;
    color: var(--mark-grey);
  }
  .card--front .brand__square { width: 18px; height: 18px; }
  .card--back .brand {
    top: 50%;
    left: 50%;
    transform: translate(-50%, -50%);
    font-size: 34px;
    color: var(--mark-silver);
  }
  .card--back .brand__square { width: 24px; height: 24px; }

  .identity {
    position: absolute;
    left: 45px;
    top: 173px;
    height: 59px;
    padding-left: 14px;
    border-left: 10px solid var(--accent);
  }
  .identity__name {
    margin: 0;
    font-size: 28px;
    font-weight: 500;
    line-height: 1.05;
    margin-top: 2px;
  }
  .identity__title {
    margin: 2px 0 0;
    font-size: 16px;
    font-weight: 500;
    color: var(--accent);
  }

  .contact {
    position: absolute;
    left: 42px;
    top: 256px;
    margin: 0;
    padding: 0;
    list-style: none;
    font-size: 16px;
    font-weight: 500;
    letter-spacing: 0.3px;
    line-height: 22px;
  }
  .contact__item {
    display: flex;
    align-items: flex-start;
    margin-bottom: 6px;
  }
  .contact__icon {
    width: 16px;
    height: 22px;
    margin-right: 4px;
    flex: none;
    fill: var(--accent);
  }
</style>
</head>
<body>
<main class="canvas">

  <section class="card card--front" aria-label="Business card front">
    <div class="brand"><span class="brand__square"></span>Ashby &amp; Lane</div>

    <div class="identity">
      <h1 class="identity__name">Your Name</h1>
      <p class="identity__title">Job Title</p>
    </div>

    <ul class="contact">
      <li class="contact__item">
        <svg class="contact__icon" viewBox="0 0 16 22" aria-hidden="true">
          <path d="M8 3a5 5 0 0 0-5 5c0 4 5 10 5 10s5-6 5-10a5 5 0 0 0-5-5zm0 7a2 2 0 1 1 0-4 2 2 0 0 1 0 4z"/>
        </svg>
        <span>00, Street Name<br>City, State 0000</span>
      </li>
      <li class="contact__item">
        <svg class="contact__icon" viewBox="0 0 16 22" aria-hidden="true">
          <path d="M1 10c0-2 3-3 7-3s7 1 7 3v2h-4v-1.5H5V12H1z"/>
          <path d="M3 13h10l1 5H2z"/>
        </svg>
        <span>phone number</span>
      </li>
      <li class="contact__item">
        <svg class="contact__icon" viewBox="0 0 16 22" aria-hidden="true">
          <path d="M1 8h14v9H1z"/>
          <path d="M1 8l7 5 7-5" fill="none" stroke="#fff" stroke-width="1.2"/>
        </svg>
        <span>youremail@xyz.com</span>
      </li>
    </ul>
  </section>

  <section class="card card--back" aria-label="Business card back">
    <div class="brand"><span class="brand__square"></span>Ashby &amp; Lane</div>
  </section>

</main>
</body>
</html>
```